Blue Heron IT Business Card - Clean, Simple

Need a simple, clean standard sized business card for an IT consulting business using existing logo and company colours. Background should be mainly white. Feel free to be creative but clean, simple, quiet design is preferred. Font is specified in logo but any sans serif fonts work.

Contact Information for card is as follows (doesn't need to be in this exact order):

Martin Calloway
Owner
martin@blueheronit.ca
705-391-2586
www.blueheronit.ca

Target Market(s)

Small to medium sized business.

Industry/Entity Type

IT Consulting

Contact Information for Business Card

Logo and contact info.

Font styles to use
Sans Serif

Colors
EE7325
F08F49
F5BC92
FAE3D3
FDF4ED

Requirements
Must have
• All white or mostly white background.

```html
<!DOCTYPE html>
<html lang="en">
<head>
<meta charset="utf-8">
<title>Blue Heron IT – Business Card</title>
<link href="https://fonts.googleapis.com/css2?family=Montserrat:wght@400;500;700&display=swap" rel="stylesheet">
<style>
  :root {
    --orange: #EE7325;
    --orange-soft: #F08F49;
    --ink: #2a2a2a;
    --paper: #ffffff;
    --stage: #3a3a3a;
  }
  * { box-sizing: border-box; margin: 0; padding: 0; }
  html, body { width: 1200px; height: 689px; overflow: hidden; }
  body {
    background: var(--stage);
    font-family: "Montserrat", Arial, sans-serif;
    position: relative;
  }
  .card {
    position: absolute;
    top: 196px;
    width: 520px;
    height: 297px;
    background: var(--paper);
    border-radius: 18px;
    overflow: hidden;
  }
  .card--front { left: 50px; }
  .card--back { left: 630px; }

  .wordmark {
    color: var(--ink);
    font-weight: 700;
    white-space: nowrap;
    display: flex;
    align-items: center;
    gap: 12px;
  }
  .wordmark__dot {
    background: var(--orange);
    border-radius: 50%;
    flex: none;
  }
  .card--front .wordmark {
    position: absolute;
    left: 0; right: 0; top: 0; bottom: 0;
    justify-content: center;
    font-size: 46px;
  }
  .card--front .wordmark__dot { width: 26px; height: 26px; }

  .card--back .wordmark {
    position: absolute;
    left: 34px;
    top: 104px;
    font-size: 22px;
    gap: 8px;
  }
  .card--back .wordmark__dot { width: 14px; height: 14px; }

  .divider {
    position: absolute;
    left: 248px;
    top: 40px;
    width: 2px;
    height: 120px;
    background: var(--orange);
  }
  .contact {
    position: absolute;
    left: 266px;
    top: 36px;
    color: var(--ink);
  }
  .contact__name {
    color: var(--orange);
    font-weight: 700;
    font-size: 20px;
    line-height: 1.1;
  }
  .contact__role {
    font-size: 12px;
    font-weight: 500;
    margin-bottom: 14px;
  }
  .contact__list { list-style: none; font-size: 12px; line-height: 1.75; }
  .contact__list li { display: flex; align-items: center; gap: 7px; }
  .contact__icon { width: 11px; height: 11px; fill: var(--orange); flex: none; }

  .swoosh { position: absolute; left: 0; bottom: 0; width: 520px; height: 297px; }
</style>
</head>
<body>
  <section class="card card--front" aria-label="Card front">
    <div class="wordmark"><span class="wordmark__dot"></span>Blue Heron IT</div>
  </section>

  <section class="card card--back" aria-label="Card back">
    <svg class="swoosh" viewBox="0 0 520 297" aria-hidden="true">
      <path d="M150 297 C 260 215, 400 190, 520 130 L520 297 Z" fill="var(--ink)"/>
      <path d="M165 297 C 270 228, 405 205, 520 150 L520 297 Z" fill="var(--paper)"/>
      <path d="M185 297 C 285 240, 410 218, 520 162 L520 297 Z" fill="var(--orange)"/>
    </svg>

    <div class="wordmark"><span class="wordmark__dot"></span>Blue Heron IT</div>

    <div class="divider"></div>

    <div class="contact">
      <p class="contact__name">Martin Calloway</p>
      <p class="contact__role">Owner</p>
      <ul class="contact__list">
        <li>
          <svg class="contact__icon" viewBox="0 0 24 24"><path d="M6.6 10.8a15.5 15.5 0 0 0 6.6 6.6l2.2-2.2a1 1 0 0 1 1-.25 11.4 11.4 0 0 0 3.6.57 1 1 0 0 1 1 1V20a1 1 0 0 1-1 1A17 17 0 0 1 3 4a1 1 0 0 1 1-1h3.5a1 1 0 0 1 1 1c0 1.25.2 2.45.57 3.57a1 1 0 0 1-.25 1z"/></svg>
          705-391-2586
        </li>
        <li>
          <svg class="contact__icon" viewBox="0 0 24 24"><path d="M2 5h20v14H2z M2 5l10 8 10-8" fill="var(--orange)"/><path d="M3 6l9 7 9-7" stroke="#fff" stroke-width="1.6" fill="none"/></svg>
          martin@blueheronit.ca
        </li>
        <li>
          <svg class="contact__icon" viewBox="0 0 24 24"><circle cx="12" cy="12" r="10"/><path d="M2 12h20M12 2c3 3 3 17 0 20M12 2c-3 3-3 17 0 20" stroke="#fff" stroke-width="1.4" fill="none"/></svg>
          www.blueheronit.ca
        </li>
      </ul>
    </div>
  </section>
</body>
</html>
```